women's junior contemporary apparel company.
We are looking for a business card that represents our urban design aesthetic. We would like to keep it simple and modern/contemporary.
the name of the company is 'v-lanza'.

we've attached a font style but you are not limited solely to use this font. All suggestions are welcomed.

```html
<!DOCTYPE html>
<html lang="en">
<head>
<meta charset="utf-8">
<title>v-lanza business card</title>
<link href="https://fonts.googleapis.com/css2?family=Ubuntu:wght@400;500;700&display=swap" rel="stylesheet">
<style>
  :root {
    --stage: #000000;
    --card-light: #f2f2f2;
    --card-mid: #c9c9c9;
    --card-edge: #a9a9a9;
    --back-light: #d2d0d0;
    --back-edge: #a8a5a5;
    --tile-blue: #0a9cf7;
    --ink: #111111;
    --ink-soft: #1b1b1b;
  }
  * { margin: 0; padding: 0; box-sizing: border-box; }
  html, body { width: 1200px; height: 900px; overflow: hidden; background: var(--stage); }
  body { position: relative; font-family: "Ubuntu", sans-serif; color: var(--ink); }

  .card-front {
    position: absolute; left: 279px; top: 42px; width: 652px; height: 372px;
    background: radial-gradient(ellipse at 50% 40%, var(--card-light) 0%, var(--card-mid) 60%, var(--card-edge) 100%);
  }
  .brand-lockup {
    position: absolute; left: 0; right: 0; top: 140px;
    display: flex; align-items: center; justify-content: center; gap: 18px;
  }
  .brand-mark { width: 34px; height: 34px; background: var(--tile-blue); }
  .brand-name { font-size: 78px; font-weight: 700; color: var(--ink); letter-spacing: 1px; line-height: 1; }
  .tagline {
    position: absolute; left: 0; right: 0; top: 301px;
    text-align: center; font-size: 19px; color: var(--ink-soft);
  }

  .card-back {
    position: absolute; left: 285px; top: 461px; width: 657px; height: 376px;
    background: radial-gradient(ellipse at 50% 45%, var(--back-light) 0%, var(--back-edge) 100%);
  }
  .tile {
    position: absolute; width: 294px; height: 147px;
    background: var(--tile-blue); border-radius: 6px;
    box-shadow: 0 3px 5px rgba(0,0,0,0.45);
    display: flex; flex-direction: column; align-items: center;
    text-align: center; font-size: 13px; color: var(--ink);
  }
  .tile-phone   { left: 28px;  top: 33px; }
  .tile-brand   { left: 337px; top: 33px; justify-content: center; }
  .tile-email   { left: 28px;  top: 195px; }
  .tile-address { left: 337px; top: 195px; }
  .tile svg { margin-top: 24px; }
  .tile-phone .contact-text { margin-top: 24px; font-size: 9px; letter-spacing: 1px; }
  .tile-email .contact-text { margin-top: 18px; }
  .tile-address .contact-text { margin-top: 14px; line-height: 16px; }
  .tile-brand .brand-name { font-size: 40px; }
  .tile-brand .brand-mark { width: 20px; height: 20px; background: var(--ink); }
  .tile-brand .brand-lockup { position: static; gap: 10px; }
</style>
</head>
<body>
  <section class="card-front">
    <div class="brand-lockup">
      <span class="brand-mark"></span>
      <span class="brand-name">v-lanza</span>
    </div>
    <p class="tagline">women's junior contemporary apparel company</p>
  </section>

  <section class="card-back">
    <div class="tile tile-phone">
      <svg width="36" height="64" viewBox="0 0 36 64" aria-hidden="true">
        <rect x="1" y="1" width="34" height="62" rx="5" fill="#f4f4f4" stroke="#cfcfcf"/>
        <rect x="4" y="8" width="28" height="44" fill="#26313d"/>
        <circle cx="18" cy="57.5" r="2.6" fill="#cfcfcf"/>
      </svg>
      <span class="contact-text">+**-***-*******</span>
    </div>

    <div class="tile tile-brand">
      <div class="brand-lockup">
        <span class="brand-mark"></span>
        <span class="brand-name">v-lanza</span>
      </div>
    </div>

    <div class="tile tile-email">
      <svg width="66" height="50" viewBox="0 0 66 50" aria-hidden="true">
        <rect x="0" y="0" width="66" height="50" fill="#f1f1f1"/>
        <path d="M0 50 L33 24 L66 50 Z" fill="#e2e2e2"/>
        <path d="M0 0 L33 30 L66 0" fill="#dcdcdc" stroke="#c9c9c9"/>
      </svg>
      <span class="contact-text">yourname/company@web.com</span>
    </div>

    <div class="tile tile-address">
      <svg width="64" height="62" viewBox="0 0 64 62" aria-hidden="true">
        <path d="M4 22 L22 16 L42 22 L60 16 L60 58 L42 62 L22 56 L4 62 Z" fill="#3fae8f"/>
        <path d="M22 16 L22 56 M42 22 L42 62" stroke="#2f8e74" stroke-width="2"/>
        <path d="M32 44 C24 32 18 26 18 16 A14 14 0 0 1 46 16 C46 26 40 32 32 44 Z" fill="#f2c230"/>
        <circle cx="32" cy="16" r="6" fill="#2f8e74"/>
      </svg>
      <span class="contact-text">I could not find your Phone, Email<br>and Address, but font and format is given</span>
    </div>
  </section>
</body>
</html>
```